Financial Planning business needs a new Business Card design

We need a business card design for an Australian financial planning business. I am looking for a clean simple design

Target Market(s)

People aged 25-40

Industry/Entity Type

Financial Service

Contact Information for Business Card

On the front of the card we need the following information:
Name: Colin Merrow (First Name Green: #006838 and last name Grey: #414042)
Position: Financial Adviser
Qualifications: BEc(Hons), AdDipFS(FP), Dip FMBM, CFL®
Mobile: 0437 512 604
Email: colin@brightledgeplan.com.au

On the back of the card we need:
Postal address: PO BOX 5307, PERTH BC, WA 6849
Website: www.brightledgeplan.com.au
Text: AFS Licence No. 518760

The fields need to be able to be edited.

Font styles to use
Sans Serif

Requirements
Must have
• Information listed above

```html
<!DOCTYPE html>
<html lang="en">
<head>
<meta charset="utf-8">
<title>Brightledge Business Card</title>
<link rel="stylesheet" href="https://fonts.googleapis.com/css2?family=Open+Sans:wght@400;600;700;800&display=swap">
<style>
  :root {
    --brand-green: #066a39;
    --charcoal: #414042;
    --paper: #ffffff;
    --backdrop: #e4e4e4;
    --ink-light: #ffffff;
  }
  * { margin: 0; padding: 0; box-sizing: border-box; }
  html, body {
    width: 1200px; height: 987px; overflow: hidden;
    background: var(--backdrop);
    font-family: "Open Sans", Arial, sans-serif;
  }
  .canvas { position: relative; width: 1200px; height: 987px; }
  .card {
    position: absolute; width: 615px; height: 350px; overflow: hidden;
    box-shadow: 0 1px 4px rgba(0,0,0,0.18);
  }
  .card--front { left: 293px; top: 130px; background: var(--paper); }
  .card--back { left: 292px; top: 505px; background: var(--brand-green); }
  .card__bands { position: absolute; inset: 0; }
  .band--green { fill: var(--brand-green); }
  .band--charcoal { fill: var(--charcoal); }
  .wordmark {
    position: absolute; left: 0; right: 0; text-align: center;
    font-weight: 800; letter-spacing: 0.5px; line-height: 1;
  }
  .card--front .wordmark { top: 93px; font-size: 46px; color: var(--brand-green); }
  .card--back .wordmark { top: 147px; font-size: 54px; color: var(--ink-light); }
  .holder {
    position: absolute; right: 29px; top: 236px; text-align: right;
    color: var(--ink-light);
  }
  .holder__name { font-size: 21px; font-weight: 600; line-height: 28px; }
  .holder__role, .holder__quals { font-size: 15.5px; line-height: 22px; }
  .contact {
    position: absolute; left: 32px; top: 285px; list-style: none;
    color: var(--ink-light); font-size: 15.5px; line-height: 23px;
  }
  .contact__item { display: flex; align-items: center; gap: 9px; }
  .contact__icon { width: 13px; height: 15px; fill: none; stroke: var(--ink-light); }
  .contact__icon--mail { fill: var(--ink-light); stroke: none; }
  .postal {
    position: absolute; left: 0; right: 0; top: 274px; text-align: center;
    color: var(--ink-light); font-size: 15.5px; line-height: 22px;
  }
</style>
</head>
<body>
<main class="canvas">
  <section class="card card--front">
    <svg class="card__bands" width="615" height="350" viewBox="0 0 615 350" aria-hidden="true">
      <polygon class="band--charcoal" points="0,230 373,230 361,243 0,243"/>
      <polygon class="band--green" points="398,211 615,211 615,350 0,350 0,246 363,246"/>
    </svg>
    <div class="wordmark">BRIGHTLEDGE</div>
    <div class="holder">
      <p class="holder__name">Colin Merrow</p>
      <p class="holder__role">Financial Adviser</p>
      <p class="holder__quals">BEc(Hons), AdDipFS(FP)</p>
      <p class="holder__quals">Dip FMBM, CFL®</p>
    </div>
    <ul class="contact">
      <li class="contact__item">
        <svg class="contact__icon" viewBox="0 0 13 15" aria-hidden="true">
          <rect x="2.5" y="0.8" width="8" height="13.4" rx="1.2" stroke-width="1.5"/>
          <line x1="5" y1="11.5" x2="8" y2="11.5" stroke-width="1.2"/>
        </svg>
        <span>0437 512 604</span>
      </li>
      <li class="contact__item">
        <svg class="contact__icon contact__icon--mail" viewBox="0 0 13 15" aria-hidden="true">
          <path d="M0.5 4h12v8h-12z M0.5 4l6 4.5l6-4.5" />
        </svg>
        <span>colin@brightledgeplan.com.au</span>
      </li>
    </ul>
  </section>

  <section class="card card--back">
    <div class="wordmark">BRIGHTLEDGE</div>
    <div class="postal">
      <p>PO BOX 5307, PERTH BC, WA 6849</p>
      <p>www.brightledgeplan.com.au | AFS Licence No. 518760</p>
    </div>
  </section>
</main>
</body>
</html>
```